Website design for recruitment solutions

We connect top talents to fast growing employers in Asia. We need to revamp our existing website (currently outdated) and also add more pages to make it more informative for talents and employers.
We need final design output to be for both desktop and mobile devices. The final design output must come with all specifications so it's easier for our dev team to implement. We have a detailed mockup but we expect the design to be significantly changed by the final output. We want the pages to look aesthetic, modern and professional.
Number of Pages Required
5+ page
Requirements
Must have
- - To have Pages design for desktop+mobile. Need to take into account intermediate resolutions like 1365px\1023px\767px\479px, especially if mobile/desktop design differs considerably. Design should be repeatable (between pages), suitable for block-layout.
Nice to have
- In terms of receiving files, we usually work with designers who can deliver files in Figma or Sketch with export to Figma. If in PSD format - please export to Zeplin or Avocode, otherwise will be difficult to open

```html
<!DOCTYPE html>
<html lang="en">
<head>
<meta charset="utf-8">
<title>Hirelane – Recruitment Website Design</title>
<link rel="stylesheet" href="https://fonts.googleapis.com/css2?family=Work+Sans:wght@400;500;600&family=Montserrat:wght@400;500;600;700&display=swap">
<style>
:root{
  --brand-blue:#56729e;
  --sky:#b6d2e6;
  --red:#e8231f;
  --ink:#1f1f22;
  --white:#ffffff;
  --paper:#ffffff;
  --field-line:#e3e6ea;
  --muted:#9aa6b4;
}
*{box-sizing:border-box;margin:0;padding:0}
html,body{width:1200px;height:2166px;overflow:hidden;background:var(--paper)}
body{font-family:"Montserrat",sans-serif;color:var(--ink)}
h1,h2,h3,h4,h5{font-weight:400}
.stage{position:relative;width:1420px;height:2563px;transform:scale(.84507);transform-origin:0 0}
.frame{position:absolute;background:var(--white);overflow:hidden;box-shadow:0 10px 40px rgba(40,50,70,.18)}

/* ===== Desktop ===== */
.desktop{left:165px;top:92px;width:777px;height:2305px}
.bg-svg{position:absolute;left:0;top:0}
.logo{position:absolute;font-family:"Montserrat",sans-serif;font-weight:600;color:var(--white);letter-spacing:2px;white-space:nowrap}
.header-logo{left:82px;top:14px;font-size:14px}
.nav{position:absolute;left:231px;top:16px;display:flex;gap:14px;font-size:6.5px;letter-spacing:.6px;color:var(--white)}
.pill{position:absolute;border-radius:12px;font-size:8px;font-weight:700;color:var(--white);display:flex;align-items:center;justify-content:center}
.pill-login{left:533px;top:9px;width:70px;height:20px;background:#000}
.pill-register{left:616px;top:9px;width:79px;height:20px;background:var(--red)}
.hero-title{position:absolute;left:0;width:802px;top:145px;text-align:center;font-family:"Work Sans",sans-serif;font-weight:400;font-size:39px;line-height:40.5px;color:var(--white);letter-spacing:.6px}
.scroll-cue{position:absolute;left:380px;top:292px}
.feature-title{position:absolute;font-family:"Work Sans",sans-serif;font-weight:500;font-size:36px;line-height:46px;color:var(--brand-blue);letter-spacing:.5px}
.feature-title.dark{color:var(--ink)}
.feature-copy{position:absolute;font-size:10px;line-height:17.4px;color:var(--ink)}
.red-rule{position:absolute;width:2px;background:var(--red)}
.photo{position:absolute}
.testimonials-title{position:absolute;left:0;width:822px;top:1430px;text-align:center;font-family:"Work Sans",sans-serif;font-weight:400;font-size:19px;color:var(--brand-blue);letter-spacing:.4px}
.testimonial-card{position:absolute;left:101px;top:1483px;width:570px;height:102px;background:var(--white);box-shadow:0 2px 10px rgba(0,0,0,.07)}
.avatar{position:absolute;left:15px;top:23px;width:60px;height:60px;border-radius:50%;background:linear-gradient(160deg,#c8ccd2,#7d8794)}
.quote{position:absolute;left:87px;top:30px;width:470px;font-size:9.6px;line-height:17.5px;color:var(--ink)}
.stars{position:absolute;left:232px;top:73px;font-size:16px;letter-spacing:9px;color:var(--brand-blue)}
.stars .off{color:var(--sky)}
.dots{position:absolute;left:372px;top:1600px;display:flex;gap:16px}
.dots i{width:5px;height:5px;border-radius:50%;background:#c6ccd4;display:block}
.dots i.on{background:var(--brand-blue)}
.cta-title{position:absolute;left:112px;top:1752px;font-family:"Montserrat",sans-serif;font-weight:600;font-size:37px;line-height:45.5px;color:var(--white);letter-spacing:.6px}
.cta-copy{position:absolute;left:127px;top:1913px;width:400px;font-size:9.8px;line-height:15px;color:var(--white)}
.footer-logo{left:82px;top:2098px;font-size:14px;letter-spacing:.5px;font-weight:700}
.footer-about{position:absolute;left:82px;top:2133px;width:184px;font-size:10px;line-height:14.6px;color:var(--white)}
.footer-col{position:absolute;top:2097px;font-size:9.6px;color:var(--white)}
.footer-col h4{font-weight:500;letter-spacing:2.2px;margin-bottom:21px;font-size:9.6px}
.footer-col p{line-height:14.5px}
.footer-rule{position:absolute;left:82px;top:2240px;width:614px;height:1px;background:rgba(255,255,255,.45)}
.legal{position:absolute;font-size:5.6px;font-weight:700;line-height:7px;color:var(--white)}

/* ===== Mobile ===== */
.mobile{top:92px;width:146px;height:955px}
.mobile-a{left:978px}
.mobile-b{left:1177px}
.m-logo{left:9px;top:4px;font-size:5px;letter-spacing:.8px}
.m-btn{position:absolute;top:3px;height:6px;border-radius:4px;font-size:2.6px;color:var(--white);display:flex;align-items:center;justify-content:center}
.m-btn.login{left:78px;width:20px;border:.5px solid var(--white)}
.m-btn.reg{left:101px;width:20px;background:var(--red)}
.m-burger{position:absolute;left:126px;top:4px;width:10px}
.m-burger i{display:block;height:1px;background:var(--white);margin-bottom:1.6px}
.m-hero{position:absolute;left:0;width:146px;top:22px;text-align:center;font-family:"Work Sans",sans-serif;font-size:9px;line-height:10.8px;color:var(--white)}
.m-title{position:absolute;left:10px;font-family:"Work Sans",sans-serif;font-weight:500;font-size:8.6px;line-height:10.8px;color:var(--brand-blue)}
.m-title.dark{color:var(--ink)}
.m-copy{position:absolute;left:12px;width:124px;font-size:4.2px;line-height:8.9px;color:var(--ink)}
.m-rule{position:absolute;left:9px;width:1px;background:var(--red)}
.m-card{position:absolute;left:8px;top:620px;width:129px;height:48px;background:var(--white);box-shadow:0 1px 4px rgba(0,0,0,.08)}
.m-card .m-avatar{position:absolute;left:59px;top:3px;width:10px;height:10px;border-radius:50%;background:#8e97a3}
.m-card p{position:absolute;left:6px;top:16px;width:117px;font-size:3.3px;line-height:6.6px;text-align:center}
.m-cta{position:absolute;left:11px;top:726px;font-weight:600;font-size:8.2px;line-height:10.6px;color:var(--white)}
.m-cta-copy{position:absolute;left:14px;top:766px;width:116px;font-size:3.4px;line-height:5.6px;color:var(--white)}
.m-foot-logo{left:8px;top:808px;font-size:6.4px;font-weight:700;letter-spacing:.3px}
.m-foot-about{position:absolute;left:8px;top:820px;width:130px;font-size:3.9px;line-height:6.8px;color:var(--white)}
.m-foot-cols{position:absolute;left:8px;top:865px;display:flex;gap:10px;font-size:3px;color:var(--white)}
.m-foot-cols h5{font-weight:500;letter-spacing:.6px;margin-bottom:3px;font-size:3px}
.m-legal{position:absolute;left:8px;width:130px;font-size:3px;line-height:4px;color:var(--white)}
.m-menu{position:absolute;left:0;top:0;width:64px;height:237px;background:var(--brand-blue);box-shadow:2px 0 5px rgba(0,0,0,.15)}
.m-menu ul{list-style:none;position:absolute;left:8px;top:16px;font-size:3.4px;line-height:4px;color:var(--white)}
.m-close{position:absolute;left:57px;top:2px;font-size:6px;color:var(--white);line-height:1}

/* ===== Form ===== */
.form-card{left:978px;top:1135px;width:345px;height:442px}
.form-title{position:absolute;left:24px;top:24px;font-family:"Work Sans",sans-serif;font-weight:400;font-size:24px;color:var(--brand-blue);letter-spacing:.3px}
.field{position:absolute;left:29px;width:292px;height:19px;border:1px solid var(--field-line);font-size:7.2px;padding:5px 0 0 12px;color:var(--ink)}
.field.area{height:103px;padding:5px 0 0 7px}
.upload-label{position:absolute;left:29px;top:331px;font-size:7.2px}
.upload{position:absolute;left:29px;top:346px;width:292px;height:20px;border:1px solid var(--field-line)}
.upload span{position:absolute;left:0;top:0;width:54px;height:18px;background:var(--sky);font-size:7px;padding:5px 0 0 8px}
.form-note{position:absolute;left:31px;top:381px;font-size:6.8px}
.submit{position:absolute;left:29px;top:399px;width:297px;height:20px;background:var(--red);color:var(--white);font-size:7px;font-weight:700;display:flex;align-items:center;justify-content:center}
</style>
</head>
<body>
<div class="stage">

  <!-- Desktop page -->
  <section class="frame desktop" aria-label="Desktop home page">
    <svg class="bg-svg" width="777" height="2305" viewBox="0 0 777 2305" aria-hidden="true">
      <polygon points="0,0 777,0 777,364 0,410" fill="#56729e"/>
      <polygon points="0,793 777,734 777,1075 0,1128" fill="#b6d2e6"/>
      <polygon points="0,2053 777,1984 777,2305 0,2305" fill="#56729e"/>
    </svg>

    <div class="logo header-logo">HIRELANE</div>
    <nav class="nav"><span>HOME</span><span>HOW WE WORK</span><span>BROWSE JOBS</span><span>EMPLOYERS</span><span>ABOUT US</span></nav>
    <div class="pill pill-login">Login</div>
    <div class="pill pill-register">Register</div>

    <h1 class="hero-title">We connect top talents<br>into fast growing<br>employers in Asia.</h1>
    <svg class="scroll-cue" width="16" height="16" viewBox="0 0 16 16" aria-hidden="true">
      <circle cx="8" cy="8" r="7.5" fill="#fff"/>
      <path d="M8 3.5v8M5 8.6l3 3 3-3" stroke="#56729e" stroke-width="1.3" fill="none"/>
    </svg>

    <h2 class="feature-title" style="left:107px;top:482px">Smart<br>Connections</h2>
    <div class="red-rule" style="left:104px;top:581px;height:67px"></div>
    <p class="feature-copy" style="left:122px;top:580px;width:256px">It's the quality of the connection that matters. Our role matching algorithms and talent managers work around theclock to find opportunities suitable to your unique profile.</p>
    <div class="photo" role="img" aria-label="Green digital code streaming on a dark screen" style="left:389px;top:462px;width:307px;height:241px;background:linear-gradient(90deg,#041006,#0f4a18 20%,#051408 35%,#1a6a24 55%,#041006 70%,#0e4716 85%,#030a04)"></div>

    <div class="photo" role="img" aria-label="Laptop showing an analytics dashboard with blue charts" style="left:81px;top:824px;width:284px;height:189px;background:linear-gradient(135deg,#e9dfe3 0%,#1b1f26 18%,#0e1218 60%,#1d7fa0 80%,#eadfe4 100%)"></div>
    <h2 class="feature-title dark" style="left:409px;top:820px">Critical<br>insights</h2>
    <div class="red-rule" style="left:408px;top:920px;height:92px"></div>
    <p class="feature-copy" style="left:432px;top:917px;width:240px">Our close interactions with candidates and employers have helped us create a comprehensive database ofcompanies, talents and skills. With HIRELANE, you will gain full access to timely intel to help you make the right career decision.</p>

    <h2 class="feature-title" style="left:107px;top:1164px;font-weight:600">People<br>First</h2>
    <div class="red-rule" style="left:104px;top:1263px;height:82px"></div>
    <p class="feature-copy" style="left:122px;top:1262px;width:226px">We take the time to really understand you holistically as a person to maximize your potential. As your careercounselor, we provide maximum transparency and feedback throughout the process.</p>
    <div class="photo" role="img" aria-label="Developer working at a computer in an office" style="left:359px;top:1158px;width:337px;height:209px;background:linear-gradient(100deg,#3b3a3a 0%,#2a2d36 35%,#57657a 60%,#c9a35a 85%,#d8d8d8 100%)"></div>

    <h3 class="testimonials-title">What They Say About Us</h3>
    <div class="testimonial-card">
      <div class="avatar" role="img" aria-label="Portrait of a client"></div>
      <p class="quote">We take the time to really understand you holistically as a person to maximize your potential. As your careercounselor, we provide maximum transparency and feedback throughout the process.</p>
      <div class="stars">★★★★<span class="off">★</span></div>
    </div>
    <div class="dots"><i class="on"></i><i></i><i></i></div>

    <svg class="bg-svg" width="777" height="2305" viewBox="0 0 777 2305" role="img" aria-label="Smiling young professional woman in a bright office">
      <defs>
        <linearGradient id="ctaTone" x1="0" y1="0" x2="1" y2="0">
          <stop offset="0" stop-color="#4f6f92"/>
          <stop offset=".55" stop-color="#6d8aa6"/>
          <stop offset="1" stop-color="#a7b6c6"/>
        </linearGradient>
      </defs>
      <polygon points="0,1690 777,1614 777,1984 0,2053" fill="url(#ctaTone)"/>
    </svg>
    <h2 class="cta-title">Work with our<br>passionate machine<br>and humans.</h2>
    <div class="red-rule" style="left:110px;top:1913px;height:45px"></div>
    <p class="cta-copy">By joining HIRELANE, we will start actively matching you to exciting opportunities. We also take your personalinformation very seriously and we do not share your profile with the employers unless we receive your explicitapproval.</p>

    <div class="logo footer-logo">HIRELANE</div>
    <p class="footer-about">Hirelane is a modern recruitment partner for high potential technology and finance talents.  We work closely with hedge funds, systemic trading and Fintech employers experiencing hyper growth in Asia</p>
    <div class="footer-col" style="left:292px"><h4>TALENTS</h4><p>How We Work<br>Browse Jobs</p></div>
    <div class="footer-col" style="left:412px"><h4>EMPLOYERS</h4><p>Why HIRELANE</p></div>
    <div class="footer-col" style="left:552px"><h4>ABOUT US</h4><p>About HIRELANE<br>Working at HIRELANE</p></div>
    <div class="footer-rule"></div>
    <p class="legal" style="left:82px;top:2273px">© Hirelane 2012-2020. All rights reserved.</p>
    <p class="legal" style="left:289px;top:2262px">Northbay Partners Limited (EA License No. 40211)<br>Room 12, Level 4, Harbour Tower C, 88 Harbour Road,<br>Wan Chai, Hong Kong</p>
    <p class="legal" style="left:515px;top:2269px">Hirelane Pte. Ltd. (License No. 2046318)<br>42 Marina Way, #10-02 Bay Centre, Singapore 018900</p>
  </section>

  <!-- Mobile page -->
  <section class="frame mobile mobile-a" aria-label="Mobile home page">
    <svg class="bg-svg" width="146" height="955" viewBox="0 0 146 955" aria-hidden="true">
      <polygon points="0,0 146,0 146,64 0,70" fill="#56729e"/>
      <polygon points="0,250 146,243 146,440 0,440" fill="#b6d2e6"/>
      <polygon points="0,793 146,793 146,955 0,955" fill="#56729e"/>
    </svg>
    <div class="logo m-logo">HIRELANE</div>
    <div class="m-btn login">Login</div><div class="m-btn reg">Register</div>
    <div class="m-burger"><i></i><i></i><i></i></div>
    <p class="m-hero">We connect top talents<br>into fast growing<br>employers in Asia.</p>
    <h2 class="m-title" style="top:90px">Smart<br>Connections</h2>
    <div class="m-rule" style="top:116px;height:34px"></div>
    <p class="m-copy" style="top:114px">It's the quality of the connection that matters. Our role matching algorithms and talent managers work around theclock to find opportunities suitable to your unique profile.</p>
    <div class="photo" role="img" aria-label="Green digital code streaming on a dark screen" style="left:8px;top:157px;width:129px;height:80px;background:linear-gradient(90deg,#041006,#1a6a24 30%,#051408 50%,#176020 75%,#030a04)"></div>
    <div class="photo" role="img" aria-label="Laptop showing an analytics dashboard" style="left:8px;top:268px;width:129px;height:84px;background:linear-gradient(135deg,#e9dfe3,#151a22 25%,#1d7fa0 75%,#eadfe4)"></div>
    <h2 class="m-title dark" style="top:366px">Critical<br>insights</h2>
    <div class="m-rule" style="top:393px;height:40px"></div>
    <p class="m-copy" style="top:391px">Our close interactions with candidates and employers have helped us create a comprehensive database ofcompanies, talents and skills. With HIRELANE, you will gain full access to timely intel to help you make the right career decision.</p>
    <h2 class="m-title" style="top:458px">People<br>First</h2>
    <div class="m-rule" style="top:488px;height:32px"></div>
    <p class="m-copy" style="top:486px">We take the time to really understand you holistically as a person to maximize your potential. As your careercounselor, we provide maximum transparency and feedback throughout the process.</p>
    <div class="photo" role="img" aria-label="Developer working at a computer" style="left:10px;top:535px;width:127px;height:73px;background:linear-gradient(100deg,#3b3a3a,#2a2d36 40%,#57657a 65%,#c9a35a 90%)"></div>
    <div class="m-card"><div class="m-avatar" role="img" aria-label="Portrait of a client"></div><p>We take the time to really understand you holistically as a person to maximize your potential. As your careercounselor, we provide maximum transparency and feedback throughout the process.</p></div>
    <svg class="bg-svg" width="146" height="955" viewBox="0 0 146 955" role="img" aria-label="Smiling young professional woman in an office">
      <polygon points="0,702 146,691 146,793 0,793" fill="#6a87a3"/>
    </svg>
    <h2 class="m-cta">Work with our<br>passionate machine<br>and humans.</h2>
    <p class="m-cta-copy">By joining HIRELANE, we will start actively matching you to exciting opportunities. We also take your personalinformation very seriously.</p>
    <div class="logo m-foot-logo">HIRELANE</div>
    <p class="m-foot-about">Hirelane is a modern recruitment partner for high potential technology and finance talents. We work closely with hedge funds, systemic trading and Fintech employers experiencing hyper growth in Asia</p>
    <div class="m-foot-cols"><div><h5>TALENTS</h5>How We Work<br>Browse Jobs</div><div><h5>EMPLOYERS</h5>Why HIRELANE</div><div><h5>ABOUT US</h5>About HIRELANE<br>Working at HIRELANE</div></div>
    <p class="m-legal" style="top:903px">Northbay Partners Limited (EA License No. 40211)<br>Room 12, Level 4, Harbour Tower C, 88 Harbour Road,<br>Wan Chai, Hong Kong</p>
    <p class="m-legal" style="top:922px">Hirelane Pte. Ltd. (License No. 2046318)<br>42 Marina Way, #10-02 Bay Centre, Singapore 018900</p>
    <p class="m-legal" style="top:942px">© Hirelane 2012-2020. All rights reserved.</p>
  </section>

  <!-- Mobile page with open menu -->
  <section class="frame mobile mobile-b" aria-label="Mobile home page with open menu">
    <svg class="bg-svg" width="146" height="955" viewBox="0 0 146 955" aria-hidden="true">
      <polygon points="0,0 146,0 146,64 0,70" fill="#56729e"/>
      <polygon points="0,250 146,243 146,440 0,440" fill="#b6d2e6"/>
      <polygon points="0,793 146,793 146,955 0,955" fill="#56729e"/>
    </svg>
    <div class="m-btn login">Login</div><div class="m-btn reg">Register</div>
    <div class="m-burger"><i></i><i></i><i></i></div>
    <p class="m-hero">We connect top talents<br>into fast growing<br>employers in Asia.</p>
    <h2 class="m-title" style="top:90px">Smart<br>Connections</h2>
    <p class="m-copy" style="top:114px">It's the quality of the connection that matters. Our role matching algorithms and talent managers work around theclock to find opportunities suitable to your unique profile.</p>
    <div class="photo" role="img" aria-label="Green digital code streaming on a dark screen" style="left:8px;top:157px;width:129px;height:80px;background:linear-gradient(90deg,#041006,#1a6a24 30%,#051408 50%,#176020 75%,#030a04)"></div>
    <div class="m-menu">
      <span class="m-close">×</span>
      <ul><li>Home</li><li>How We Work</li><li>Browse Jobs</li><li>Employers</li><li>About Us</li></ul>
    </div>
    <div class="photo" role="img" aria-label="Laptop showing an analytics dashboard" style="left:8px;top:268px;width:129px;height:84px;background:linear-gradient(135deg,#e9dfe3,#151a22 25%,#1d7fa0 75%,#eadfe4)"></div>
    <h2 class="m-title dark" style="top:366px">Critical<br>insights</h2>
    <div class="m-rule" style="top:393px;height:40px"></div>
    <p class="m-copy" style="top:391px">Our close interactions with candidates and employers have helped us create a comprehensive database ofcompanies, talents and skills. With HIRELANE, you will gain full access to timely intel to help you make the right career decision.</p>
    <h2 class="m-title" style="top:458px">People<br>First</h2>
    <div class="m-rule" style="top:488px;height:32px"></div>
    <p class="m-copy" style="top:486px">We take the time to really understand you holistically as a person to maximize your potential. As your careercounselor, we provide maximum transparency and feedback throughout the process.</p>
    <div class="photo" role="img" aria-label="Developer working at a computer" style="left:10px;top:535px;width:127px;height:73px;background:linear-gradient(100deg,#3b3a3a,#2a2d36 40%,#57657a 65%,#c9a35a 90%)"></div>
    <div class="m-card"><div class="m-avatar" role="img" aria-label="Portrait of a client"></div><p>We take the time to really understand you holistically as a person to maximize your potential. As your careercounselor, we provide maximum transparency and feedback throughout the process.</p></div>
    <svg class="bg-svg" width="146" height="955" viewBox="0 0 146 955" role="img" aria-label="Smiling young professional woman in an office">
      <polygon points="0,702 146,691 146,793 0,793" fill="#6a87a3"/>
    </svg>
    <h2 class="m-cta">Work with our<br>passionate machine<br>and humans.</h2>
    <p class="m-cta-copy">By joining HIRELANE, we will start actively matching you to exciting opportunities. We also take your personalinformation very seriously.</p>
    <div class="logo m-foot-logo">HIRELANE</div>
    <p class="m-foot-about">Hirelane is a modern recruitment partner for high potential technology and finance talents. We work closely with hedge funds, systemic trading and Fintech employers experiencing hyper growth in Asia</p>
    <div class="m-foot-cols"><div><h5>TALENTS</h5>How We Work<br>Browse Jobs</div><div><h5>EMPLOYERS</h5>Why HIRELANE</div><div><h5>ABOUT US</h5>About HIRELANE<br>Working at HIRELANE</div></div>
    <p class="m-legal" style="top:903px">Northbay Partners Limited (EA License No. 40211)<br>Room 12, Level 4, Harbour Tower C, 88 Harbour Road,<br>Wan Chai, Hong Kong</p>
    <p class="m-legal" style="top:922px">Hirelane Pte. Ltd. (License No. 2046318)<br>42 Marina Way, #10-02 Bay Centre, Singapore 018900</p>
    <p class="m-legal" style="top:942px">© Hirelane 2012-2020. All rights reserved.</p>
  </section>

  <!-- Sign-up form -->
  <section class="frame form-card" aria-label="Sign-up form">
    <h2 class="form-title">Team up with us!</h2>
    <div class="field" style="top:69px">Full Name</div>
    <div class="field" style="top:108px">Email</div>
    <div class="field" style="top:147px">Phone</div>
    <div class="field" style="top:186px">Profile Url</div>
    <div class="field area" style="top:219px">What are you looking for?</div>
    <div class="upload-label">Upload Your CV</div>
    <div class="upload"><span>Browse</span></div>
    <p class="form-note">Don't worry! We will keep your profile strictly confidential until we speak.</p>
    <div class="submit">Get Started</div>
  </section>

</div>
</body>
</html>
```